Automotive parts Package (box) design

We are developing a new packaging concept for our automotive service and suspension parts line. I will share 2–3 sample designs—some from other brands and some AI‑generated—and we need a designer to create a unified, original design direction based on these references.

We already have an established brand name, VEK, along with a logo. The logo may be updated or redesigned, but the brand name VEK must remain.

- The project includes creating the full packaging design for our product boxes, developing or refining the logo if needed.

-Then, after choosing the design, we will apply the same design to 8 boxes with small customisation for each box to match the product.

- The box die-lines will be provided by us.

Attached are a few sample designs. We need you to develop three or more new designs in a similar style. If you have additional creative concepts beyond these references, you are welcome to include them. The only fixed requirement is that the brand name VEK must remain unchanged in all proposed designs.

Box files such as PNG, PDF (ready-to-print file) and Ai (Editable/ Source file) and fonts with 3D mockup images at the end of the project must be given to us.

Target Market(s)

Car spare parts shops

Industry/Entity Type

Auto Parts

Requirements
Must have
• Our brand name VEK
Nice to have
• Package similar to big auto parts suppliers such as MLP, KRUVE

```html
<!DOCTYPE html>
<html lang="en">
<head>
<meta charset="utf-8">
<title>VEK Service Parts – Box Artwork</title>
<link rel="stylesheet" href="https://fonts.googleapis.com/css2?family=Exo+2:wght@700;800;900&display=swap">
<style>
  :root {
    --bg: #e4e4e6;
    --panel-black: #1c1c1e;
    --panel-black-2: #2a2a2d;
    --red: #e3262b;
    --red-dark: #8e1518;
    --silver: #a9abb0;
    --silver-light: #d9dadc;
    --white: #ffffff;
  }
  * { box-sizing: border-box; margin: 0; padding: 0; }
  html, body { width: 1200px; height: 912px; overflow: hidden; }
  body {
    background: var(--bg);
    font-family: "Exo 2", sans-serif;
    position: relative;
  }
  .panel {
    position: absolute;
    background: linear-gradient(160deg, var(--panel-black-2), var(--panel-black) 60%);
    overflow: hidden;
    box-shadow: 0 8px 24px rgba(0,0,0,0.18);
  }
  .panel--top   { left: 50px;  top: 50px;  width: 780px; height: 430px; }
  .panel--front { left: 50px;  top: 500px; width: 780px; height: 360px; }
  .panel--end   { left: 850px; top: 50px;  width: 300px; height: 810px; }

  .band { position: absolute; inset: 0; width: 100%; height: 100%; }

  .product-art {
    position: absolute;
    background: linear-gradient(100deg, rgba(255,255,255,0.02), rgba(160,162,168,0.16) 50%, rgba(255,255,255,0.02));
    border-radius: 40px;
  }
  .panel--top .product-art   { left: 150px; top: 110px; width: 480px; height: 80px; transform: rotate(-22deg); }
  .panel--front .product-art { left: 160px; top: 100px; width: 470px; height: 70px; transform: rotate(-14deg); }

  .brand {
    position: absolute;
    display: flex; align-items: center; gap: 12px;
    color: var(--silver-light);
    font-weight: 900;
    letter-spacing: 2px;
    line-height: 1;
  }
  .brand__mark { background: var(--red); display: block; }
  .panel--top .brand   { left: 60px; top: 150px; font-size: 74px; }
  .panel--top .brand__mark { width: 26px; height: 26px; }
  .panel--front .brand { left: 70px; top: 110px; font-size: 60px; }
  .panel--front .brand__mark { width: 22px; height: 22px; }

  .service-title {
    position: absolute;
    color: var(--silver);
    font-weight: 900;
    letter-spacing: 3px;
    text-transform: uppercase;
    white-space: nowrap;
  }
  .panel--top .service-title   { left: 290px; top: 240px; font-size: 50px; }
  .panel--front .service-title { left: 270px; top: 165px; font-size: 44px; }

  .tagline {
    position: absolute;
    color: var(--white);
    font-weight: 800;
    letter-spacing: 2px;
    text-transform: uppercase;
    white-space: nowrap;
  }
  .panel--top .tagline   { left: 150px; top: 360px; font-size: 32px; }
  .panel--front .tagline { left: 140px; top: 290px; font-size: 30px; }

  .warranty {
    position: absolute;
    width: 118px; height: 118px;
    border-radius: 50%;
    background: radial-gradient(circle at 35% 30%, #f4f4f5, #9c9ea3 70%, #6d6f74);
    border: 5px solid #3b3c40;
    display: flex; flex-direction: column; align-items: center; justify-content: center;
    color: #222;
    text-transform: uppercase;
    line-height: 1;
  }
  .warranty__num { font-size: 40px; font-weight: 900; }
  .warranty__label { font-size: 11px; font-weight: 800; letter-spacing: 1px; margin-top: 2px; }
  .warranty__ribbon {
    margin-top: 4px; background: #2c2d30; color: var(--white);
    font-size: 11px; font-weight: 800; letter-spacing: 1px; padding: 3px 8px;
  }
  .panel--top .warranty   { right: 50px; top: 110px; }
  .panel--front .warranty { right: 50px; top: 60px; }

  .end-brand {
    position: absolute; left: 30px; top: 250px;
    display: flex; align-items: center; gap: 12px;
    color: var(--silver-light); font-size: 96px; font-weight: 900; letter-spacing: 3px; line-height: 1;
  }
  .end-brand .brand__mark { width: 28px; height: 28px; }
  .end-sub {
    position: absolute; left: 30px; top: 360px;
    color: var(--silver-light); font-size: 17px; font-weight: 800; letter-spacing: 1px; text-transform: uppercase;
  }
  .end-title {
    position: absolute; left: 30px; top: 520px;
    color: var(--white); font-size: 40px; font-weight: 900; letter-spacing: 2px; text-transform: uppercase; line-height: 1.05;
  }
</style>
</head>
<body>

  <section class="panel panel--top">
    <div class="product-art" role="img" aria-label="Line drawing of a steering rack with rubber boots"></div>
    <svg class="band" viewBox="0 0 780 430" preserveAspectRatio="none" aria-hidden="true">
      <defs>
        <linearGradient id="redTop" x1="0" y1="0" x2="1" y2="0">
          <stop offset="0" stop-color="#e3262b"/><stop offset="1" stop-color="#8e1518"/>
        </linearGradient>
      </defs>
      <polygon points="0,330 560,330 620,250 780,250 780,430 0,430" fill="url(#redTop)"/>
      <polyline points="0,322 556,322 616,242 780,242" fill="none" stroke="#6c6e73" stroke-width="4"/>
      <polygon points="0,0 780,0 780,14 0,14" fill="url(#redTop)"/>
    </svg>
    <div class="brand"><span class="brand__mark"></span>VEK</div>
    <div class="service-title">Service Parts</div>
    <div class="tagline">VEK Automotive Components</div>
    <div class="warranty">
      <span class="warranty__num">6</span>
      <span class="warranty__label">Month</span>
      <span class="warranty__ribbon">Warranty</span>
    </div>
  </section>

  <section class="panel panel--front">
    <div class="product-art" role="img" aria-label="Line drawing of a steering rack with rubber boots"></div>
    <svg class="band" viewBox="0 0 780 360" preserveAspectRatio="none" aria-hidden="true">
      <defs>
        <linearGradient id="redFront" x1="0" y1="0" x2="1" y2="0">
          <stop offset="0" stop-color="#e3262b"/><stop offset="1" stop-color="#8e1518"/>
        </linearGradient>
      </defs>
      <polygon points="0,0 780,0 780,14 0,14" fill="url(#redFront)"/>
      <polygon points="0,270 560,270 620,200 780,200 780,360 0,360" fill="url(#redFront)"/>
      <polyline points="0,262 556,262 616,192 780,192" fill="none" stroke="#6c6e73" stroke-width="4"/>
    </svg>
    <div class="brand"><span class="brand__mark"></span>VEK</div>
    <div class="service-title">Service Parts</div>
    <div class="tagline">VEK Automotive Components</div>
    <div class="warranty">
      <span class="warranty__num">6</span>
      <span class="warranty__label">Month</span>
      <span class="warranty__ribbon">Warranty</span>
    </div>
  </section>

  <section class="panel panel--end">
    <svg class="band" viewBox="0 0 300 810" preserveAspectRatio="none" aria-hidden="true">
      <defs>
        <linearGradient id="redEnd" x1="0" y1="0" x2="1" y2="0">
          <stop offset="0" stop-color="#e3262b"/><stop offset="1" stop-color="#a5181c"/>
        </linearGradient>
      </defs>
      <rect x="0" y="0" width="300" height="150" fill="url(#redEnd)"/>
      <rect x="0" y="470" width="300" height="340" fill="url(#redEnd)"/>
      <line x1="0" y1="462" x2="300" y2="462" stroke="#6c6e73" stroke-width="4"/>
    </svg>
    <div class="end-brand"><span class="brand__mark"></span>VEK</div>
    <div class="end-sub">VEK Automotive Components</div>
    <div class="end-title">Service<br>Parts</div>
  </section>

</body>
</html>
```